Creative Web Designer: Refresh & Elevate our Beach Lifestyle Brand with a Joyful, Elegant Red...

Corallune (corallune.gr), a vibrant Greek brand celebrated for its high-quality beachwear and accessories, is embarking on an exciting phase as we enter our third year. Renowned for our stylish flip flops, beach towels, and caps, we are thrilled to announce the expansion of our product line with innovative beach essentials and a fresh palette for our existing collection.
As we continue to grow and evolve, we are in search of a talented and imaginative web designer who can capture the essence of Corallune and translate it into a digital experience. Our ideal candidate will craft a website that mirrors the happiness and relaxation of a day at the beach, while also embodying the sophistication and elegance that our brand represents.
Your Mission:
Design a Website That Reflects Our Brand Identity: Create a website that is visually stunning, easy to navigate, and showcases our products in a way that feels both refreshing and luxurious.
Incorporate New Product Lines and Colors: Seamlessly integrate our new beach products and color schemes, ensuring the website remains cohesive and on-brand.
User Experience is Key: Design a user-friendly interface that ensures a seamless shopping experience for our customers, with intuitive navigation and a mobile-responsive design.
Embrace Creativity While Staying Elegant: We want our website to be a reflection of the joy and elegance that our products bring to our customers. Your design should be innovative, incorporating modern web design trends that align with our brand's aesthetic.
What We're Looking For:
A portfolio that demonstrates experience in creating visually appealing and user-friendly e-commerce websites.
Strong understanding of branding and the ability to translate a brand's essence into a digital format.
Proficiency in the latest web design software and technologies.
Excellent communication skills and the ability to work collaboratively with our team to bring our vision to life.
This is a fantastic opportunity for a web designer who loves the beach lifestyle and is passionate about creating beautiful, effective websites. If you're ready to dive into a project that will challenge and excite you, while making a significant impact on our growing brand, we would love to hear from you.
Regarding the products, on the website (corallune.gr) you will the flips flops and on the attached powerpoint all the accessories for this summer. Please use the images to craft your designs.
Join us in making Corallune the go-to brand for beach enthusiasts everywhere. Apply now to start the conversation and share your vision for our new website 😊🩴☀️⛱️
p.s. we didn;t mention the pages to be designed. Its 4 pages in all,
homepage, product category page, singleproduct page and contact us page

```html
<!DOCTYPE html>
<html lang="en">
<head>
<meta charset="utf-8">
<title>Corallune – Summerwear</title>
<link href="https://fonts.googleapis.com/css2?family=Bebas+Neue&family=Ubuntu:wght@400;500;700&display=swap" rel="stylesheet">
<style>
:root{
  --ink:#2b2265;
  --ink-deep:#241c58;
  --accent:#f5d90a;
  --card:#ebebf2;
  --line:#cfcfe0;
  --white:#ffffff;
  --text:#2a2a3a;
  --star:#e7b416;
}
*{box-sizing:border-box;margin:0;padding:0}
html,body{width:1200px;height:3062px;overflow:hidden;background:var(--white)}
body{font-family:"Ubuntu",sans-serif;color:var(--text)}
.page{position:relative;width:1200px;height:3062px;overflow:hidden}
.abs{position:absolute}
.display{font-family:"Bebas Neue",sans-serif;color:var(--ink);font-weight:400;letter-spacing:.2px}

/* top bar */
.topbar{left:0;top:0;width:1200px;height:31px;background:var(--ink);color:var(--white);font-size:11px;display:flex;align-items:center;justify-content:space-between;padding:0 150px}
.topbar span{display:flex;align-items:center;gap:7px}
.topbar .dot{width:11px;height:11px;border-radius:3px;background:var(--accent)}

/* header */
.menu-btn{left:150px;top:53px;width:40px;height:30px;border-radius:4px;background:var(--ink)}
.brand{left:450px;top:42px;width:300px;text-align:center;color:var(--ink)}
.brand .name{font-size:36px;font-weight:500;line-height:1;letter-spacing:-.5px}
.brand .sub{font-size:11px;letter-spacing:2.5px;margin-top:2px}
.cart{left:928px;top:54px;width:30px;height:28px}
.cart-count{left:948px;top:52px;width:12px;height:12px;border-radius:50%;background:var(--accent);font-size:8px;text-align:center;line-height:12px;color:var(--ink)}
.pill{display:flex;align-items:center;justify-content:center;gap:8px;border-radius:20px;font-size:11px;font-weight:500}
.pill.outline{border:1.5px solid var(--ink);background:var(--white);color:var(--ink)}
.pill.solid{background:var(--ink);color:var(--white)}
.signup{left:969px;top:53px;width:81px;height:30px;font-size:12px}

/* hero */
.hero{left:150px;top:107px;width:900px;height:144px;border:2px solid var(--ink);border-radius:10px;background:linear-gradient(120deg,#f1f0f4,#e6e5ec 50%,#f1f0f4);text-align:center}
.hero h1{font-family:"Bebas Neue",sans-serif;font-weight:400;font-size:46px;color:var(--ink);margin-top:24px;line-height:1}
.hero p{font-size:11px;line-height:14px;width:670px;margin:10px auto 0;color:var(--text)}
.shop-hero{left:540px;top:237px;width:120px;height:29px}

/* carousel */
.slide{top:311px;height:251px;width:158px;border-radius:8px;overflow:hidden}
.slide .label{position:absolute;left:12px;bottom:26px;font-family:"Bebas Neue",sans-serif;font-size:22px;color:var(--white)}
.slide.active{top:292px;width:194px;height:288px}
.slide.active .overlay{position:absolute;inset:0;background:rgba(130,60,110,.45)}
.slide.active .big{position:absolute;left:0;right:0;top:116px;text-align:center;font-family:"Bebas Neue",sans-serif;font-size:50px;color:var(--white)}
.arrow{width:22px;height:22px;border-radius:50%;background:var(--ink);top:433px}
.see-slide{left:540px;top:566px;width:121px;height:30px}

/* values band */
.values{left:0;top:622px;width:1200px;height:150px;background:linear-gradient(180deg,#a9c4dc 0%,#cfdfec 45%,#9fbbd6 100%)}
.value{top:650px;width:280px}
.value h3{font-family:"Bebas Neue",sans-serif;font-weight:400;font-size:20px;color:var(--ink);line-height:1}
.value p{font-size:10.5px;line-height:13.5px;margin-top:10px;color:#222}

/* section headings */
.sec-title{left:150px;font-size:34px;line-height:1}
.see-all{left:931px;width:119px;height:29px}

/* product card */
.card{background:var(--card);border-radius:6px;overflow:hidden}
.card .img{width:100%}
.card .info{padding:6px 7px}
.card .row{display:flex;justify-content:space-between;font-weight:500;color:var(--ink-deep)}
.card .meta{color:#555}
.card .stars{color:var(--star)}
.card .stars em{font-style:normal;color:#555}
.card .cta{display:inline-block;border:1px solid var(--ink);border-radius:10px;color:var(--ink)}
.heart{position:absolute;border-radius:50%;background:var(--ink);display:flex;align-items:center;justify-content:center}

.sm .img{height:109px}
.sm .row{font-size:9px}
.sm .meta{font-size:5px;margin-top:3px}
.sm .stars{font-size:6px;margin-top:1px}
.sm .cta{font-size:5px;padding:1px 5px;margin-top:3px}
.sm .heart{top:6px;right:8px;width:14px;height:14px}

.lg .img{height:229px}
.lg .info{padding:14px 13px}
.lg .row{font-size:19px}
.lg .meta{font-size:11px;margin-top:8px}
.lg .stars{font-size:15px;margin-top:4px}
.lg .cta{font-size:11px;padding:5px 13px;margin-top:8px;border-width:1.5px;border-radius:14px}
.lg .heart{top:16px;right:14px;width:30px;height:30px}

.md .img{height:139px}
.md .info{padding:8px 8px}
.md .row{font-size:12px}
.md .meta{font-size:6px;margin-top:4px}
.md .stars{font-size:7px;margin-top:2px}
.md .cta{font-size:6px;padding:2px 8px;margin-top:5px}
.md .heart{top:8px;right:8px;width:19px;height:19px}

/* promo band */
.promo{left:0;top:1252px;width:1200px;height:372px;background:var(--ink)}
.promo-title{left:150px;top:1330px;font-size:34px;color:var(--white)}
.promo-title .hl{color:var(--accent)}
.promo-text{left:150px;top:1375px;width:375px;font-size:10.5px;line-height:13.7px;color:var(--white)}
.promo-shop{left:150px;top:1468px;width:117px;height:29px}
.tile{border-radius:8px}

.cat{top:1543px;height:203px;width:291px;border-radius:8px;overflow:hidden;background:linear-gradient(135deg,#f5f5f7,#e3e3e8)}
.cat .art{position:absolute;right:0;top:0;width:170px;height:110px}
.cat .label{position:absolute;left:13px;top:140px;font-family:"Bebas Neue",sans-serif;font-size:21px;color:var(--ink)}
.cat .pill{position:absolute;right:12px;top:173px;width:118px;height:28px}

/* services */
.service{top:2368px;width:289px;height:289px;border-radius:8px;overflow:hidden;background:var(--card)}
.service .photo{height:189px}
.service h4{font-size:16px;font-weight:500;color:var(--ink-deep);margin:12px 11px 0}
.service p{font-size:9px;margin:6px 11px 0;color:#444}
.service .cta{display:inline-block;margin:12px 11px 0;border:1px solid var(--ink);border-radius:12px;font-size:9px;padding:3px 11px;color:var(--ink)}

/* footer */
.footer{left:0;top:2688px;width:1200px;height:374px;background:var(--ink);color:var(--white)}
.f-links{left:150px;top:2723px;display:flex;gap:21px;font-size:11px;font-weight:500;color:var(--white)}
.follow{left:881px;top:2720px;display:flex;align-items:center;gap:14px;font-size:11px;font-weight:500;color:var(--white)}
.follow i{display:block;width:13px;height:13px;border-radius:50%;background:var(--white)}
.rule{left:150px;width:900px;height:1px;background:#6f67a3}
.f-col{top:2783px;color:var(--white)}
.f-col h5{font-family:"Bebas Neue",sans-serif;font-weight:400;font-size:14px;margin-bottom:14px}
.f-col li{list-style:none;font-size:11px;height:27.5px}
.subscribe{left:832px;top:2807px;width:218px;height:24px;background:var(--white);border-radius:2px}
.subscribe span{position:absolute;right:3px;top:3px;height:18px;padding:0 6px;background:var(--ink);color:var(--white);font-size:10px;line-height:18px;border-radius:2px}
.app{left:832px;display:flex;align-items:center;gap:9px;font-size:11px;color:var(--white)}
.app i{display:block;width:12px;height:12px;border-radius:50%;background:var(--white)}
.copy{left:150px;top:3013px;font-size:11px;color:var(--white)}
</style>
</head>
<body>
<svg width="0" height="0" style="position:absolute">
  <symbol id="heart" viewBox="0 0 24 24"><path d="M12 20s-7-4.4-9-8.5C1.5 8.3 3.6 5 7 5c2 0 3.4 1.1 5 3 1.6-1.9 3-3 5-3 3.4 0 5.5 3.3 4 6.5-2 4.1-9 8.5-9 8.5z" fill="none" stroke="#fff" stroke-width="2.4"/></symbol>
  <symbol id="arrow" viewBox="0 0 40 10"><path d="M0 5h37M32 1l5 4-5 4" fill="none" stroke="currentColor" stroke-width="1.4"/></symbol>
</svg>

<div class="page">

  <!-- top bar -->
  <div class="abs topbar">
    <span><i class="dot"></i>+30 210 555 0142 | +30 690 555 0178</span>
    <span>info@corallune.gr<i class="dot"></i></span>
  </div>

  <!-- header -->
  <div class="abs menu-btn">
    <svg width="40" height="30" viewBox="0 0 40 30"><path d="M14 10h13M14 15h10M14 20h7" stroke="#fff" stroke-width="1.8" stroke-linecap="round"/></svg>
  </div>
  <div class="abs brand"><div class="name">Corallune</div><div class="sub">SUMMERWEAR</div></div>
  <svg class="abs cart" viewBox="0 0 30 28"><path d="M2 4h4l4 14h14l3-10H8" fill="none" stroke="#2b2265" stroke-width="2" stroke-linejoin="round"/><circle cx="12" cy="23" r="2.2" fill="#2b2265"/><circle cx="22" cy="23" r="2.2" fill="#2b2265"/></svg>
  <div class="abs cart-count">0</div>
  <div class="abs pill outline signup">Sign Up</div>

  <!-- hero -->
  <section class="abs hero" role="img" aria-label="Soft grey banner with contour line texture">
    <h1>CORALLUNE - SUMMERWEAR</h1>
    <p>It is a long established fact that a reader will be distracted by the readable content of a page when looking at its layout. The point of using Lorem Ipsum is that it has a more-or-less normal distribution of letters, as opposed to using 'Content here, content here', making it look like readable English. Many desktop publishing packages and web page editors now use</p>
  </section>
  <div class="abs pill outline shop-hero">Shop <svg width="32" height="8" style="color:#2b2265"><use href="#arrow"/></svg></div>

  <!-- carousel -->
  <div class="abs slide" style="left:162px;background:linear-gradient(180deg,#b9b9be,#5a5a60)" role="img" aria-label="Patterned jungle hat with chin cord"><span class="label">JUNGLE HATS</span></div>
  <div class="abs slide" style="left:331px;background:linear-gradient(180deg,#e4b6a6,#8e8ab0 60%,#6e6e74)" role="img" aria-label="Colourful patterned cap with purple brim"><span class="label">JOKEY CAPS</span></div>
  <div class="abs slide active" style="left:503px;background:linear-gradient(180deg,#a36a8e,#4c6fb2 50%,#b0739a)" role="img" aria-label="Blue drawstring beach bag">
    <div class="overlay"></div><span class="big">BEACH BAG</span>
  </div>
  <div class="abs slide" style="left:709px;background:linear-gradient(160deg,#e6e1dc,#d97a8a 55%,#8c8c90)" role="img" aria-label="Patterned pouch with pink shapes"><span class="label">POUCHES</span></div>
  <div class="abs slide" style="left:880px;background:linear-gradient(160deg,#9bb7c5,#c99e7a 50%,#56727e)" role="img" aria-label="Patterned bucket hat"><span class="label">BUCKETS</span></div>
  <svg class="abs arrow" style="left:151px" viewBox="0 0 22 22"><circle cx="11" cy="11" r="11" fill="#2b2265"/><path d="M15 11H7M10 8l-3 3 3 3" fill="none" stroke="#f5d90a" stroke-width="1.6"/></svg>
  <svg class="abs arrow" style="left:1027px" viewBox="0 0 22 22"><circle cx="11" cy="11" r="11" fill="#2b2265"/><path d="M7 11h8M12 8l3 3-3 3" fill="none" stroke="#f5d90a" stroke-width="1.6"/></svg>
  <div class="abs pill solid see-slide">See All <svg width="32" height="8" style="color:#fff"><use href="#arrow"/></svg></div>

  <!-- values -->
  <div class="abs values" role="img" aria-label="Blue sky with soft clouds"></div>
  <div class="abs value" style="left:163px"><h3>DESIGNED IN GREECE</h3><p>Corallune has Greek DNA. Our designs are exclusively inspired by what makes Greece so unique - its summer. Our mission is to give you a taste by wearing our flip flops.</p></div>
  <div class="abs value" style="left:467px"><h3>SUSTAINABILITY</h3><p>We care deeply about the environment in which we live and want to contribute to a more sustainable future through our efforts. Therefore, Corallune flip flops are produced from 100% recyclable, natural rubber.</p></div>
  <div class="abs value" style="left:772px"><h3>COMFORT &amp; STYLE</h3><p>Our flip flops are designed to offer you a unique sense of comfort throughout your summer experiences. Wear them to the beach, on a walk or just for a coffee or a drink with your friends</p></div>

  <!-- featured -->
  <h2 class="abs display sec-title" style="top:808px">FEATURED PRODUCTS</h2>
  <div class="abs pill solid see-all" style="top:809px">See All <svg width="32" height="8" style="color:#fff"><use href="#arrow"/></svg></div>

  <article class="abs card lg" style="left:150px;top:864px;width:350px;height:357px">
    <div class="img" style="background:linear-gradient(150deg,#d7d5d2,#f4efe6 45%,#f2c39c)" role="img" aria-label="Cream pouch with crab and coral print"></div>
    <span class="heart"><svg width="15" height="15"><use href="#heart"/></svg></span>
    <div class="info"><div class="row"><span>Pouch - Lorem Ipsum</span><span>€ 16.90</span></div>
      <div class="meta">6 Different Designs Available</div>
      <div class="stars">★★★★★ <em>(12)</em></div>
      <span class="cta">Add to cart</span></div>
  </article>

  <article class="abs card sm" style="left:519px;top:864px;width:165px;height:168px">
    <div class="img" style="background:linear-gradient(180deg,#eacfd3,#f0c98a 55%,#e7c3c6)" role="img" aria-label="Striped beach bag"></div>
    <span class="heart"><svg width="8" height="8"><use href="#heart"/></svg></span>
    <div class="info"><div class="row"><span>Bag - Lorem Ipsum</span><span>€ 16.90</span></div><div class="meta">6 Different Designs Available</div><div class="stars">★★★★★ <em>(12)</em></div><span class="cta">Add to cart</span></div>
  </article>
  <article class="abs card sm" style="left:702px;top:864px;width:165px;height:168px">
    <div class="img" style="background:linear-gradient(180deg,#7faab6,#c7b59c 55%,#8aaab2)" role="img" aria-label="Patterned bucket hat"></div>
    <span class="heart"><svg width="8" height="8"><use href="#heart"/></svg></span>
    <div class="info"><div class="row"><span>Pouch - Lorem Ipsum</span><span>€ 16.90</span></div><div class="meta">6 Different Designs Available</div><div class="stars">★★★★★ <em>(12)</em></div><span class="cta">Add to cart</span></div>
  </article>
  <article class="abs card sm" style="left:885px;top:864px;width:165px;height:168px">
    <div class="img" style="background:linear-gradient(180deg,#e6e6e8,#3f3d4e 55%,#d8d8dc)" role="img" aria-label="Dark patterned cap"></div>
    <span class="heart"><svg width="8" height="8"><use href="#heart"/></svg></span>
    <div class="info"><div class="row"><span>Pouch - Lorem Ipsum</span><span>€ 16.90</span></div><div class="meta">6 Different Designs Available</div><div class="stars">★★★★★ <em>(12)</em></div><span class="cta">Add to cart</span></div>
  </article>
  <article class="abs card sm" style="left:519px;top:1051px;width:165px;height:170px">
    <div class="img" style="background:radial-gradient(circle at 50% 50%,#e05a5a,#7bbf8e 40%,#f5b6a6 75%)" role="img" aria-label="Floral scrunchie"></div>
    <span class="heart"><svg width="8" height="8"><use href="#heart"/></svg></span>
    <div class="info"><div class="row"><span>Pouch - Lorem Ipsum</span><span>€ 16.90</span></div><div class="meta">6 Different Designs Available</div><div class="stars">★★★★★ <em>(12)</em></div><span class="cta">Add to cart</span></div>
  </article>
  <article class="abs card sm" style="left:702px;top:1051px;width:165px;height:170px">
    <div class="img" style="background:linear-gradient(180deg,#dcdcdc,#2a2a36 50%,#cfcfcf)" role="img" aria-label="Dark patterned tote bag"></div>
    <span class="heart"><svg width="8" height="8"><use href="#heart"/></svg></span>
    <div class="info"><div class="row"><span>Pouch - Lorem Ipsum</span><span>€ 16.90</span></div><div class="meta">6 Different Designs Available</div><div class="stars">★★★★★ <em>(12)</em></div><span class="cta">Add to cart</span></div>
  </article>
  <article class="abs card sm" style="left:885px;top:1051px;width:165px;height:170px">
    <div class="img" style="background:linear-gradient(170deg,#f4f4f6,#9fd6b8 40%,#c9b3e0 60%,#f4f4f6)" role="img" aria-label="Pastel striped beach towel"></div>
    <span class="heart"><svg width="8" height="8"><use href="#heart"/></svg></span>
    <div class="info"><div class="row"><span>Pouch - Lorem Ipsum</span><span>€ 16.90</span></div><div class="meta">6 Different Designs Available</div><div class="stars">★★★★★ <em>(12)</em></div><span class="cta">Add to cart</span></div>
  </article>

  <!-- promo -->
  <div class="abs promo" role="img" aria-label="Deep purple band with flowing line texture"></div>
  <h2 class="abs display promo-title" style="color:#fff">UMBRELLA &amp; <span class="hl">BEACH BAG</span></h2>
  <p class="abs promo-text">It is a long established fact that a reader will be distracted by the readable content of a page when looking at its layout. The point of using Lorem Ipsum is that it has a more-or-less normal distribution of letters, as opposed to using 'Content here, content here', making it look like readable English. Many desktop publishing packages and web page editors now use</p>
  <div class="abs pill outline promo-shop" style="border-color:#fff">Shop Now <svg width="32" height="8" style="color:#2b2265"><use href="#arrow"/></svg></div>
  <div class="abs tile" style="left:677px;top:1309px;width:286px;height:203px;background:linear-gradient(160deg,#5b88cf,#3b6ccb 60%,#4a77c9)" role="img" aria-label="Patterned beach umbrella on blue"></div>
  <div class="abs tile" style="left:615px;top:1338px;width:104px;height:143px;background:linear-gradient(180deg,#d98578,#c97466)" role="img" aria-label="Teal drawstring bag on coral"></div>
  <div class="abs tile" style="left:938px;top:1282px;width:112px;height:142px;background:linear-gradient(180deg,#df7a6c,#e8998c)" role="img" aria-label="Patterned pouch on coral"></div>

  <div class="abs cat" style="left:150px"><div class="art" style="background:linear-gradient(200deg,#e9a0a6,#d55a74 60%,transparent)" role="img" aria-label="Pink patterned pouch"></div><span class="label">POUCHES - CORALLUNE</span><span class="pill outline">Shop Now <svg width="32" height="8" style="color:#2b2265"><use href="#arrow"/></svg></span></div>
  <div class="abs cat" style="left:455px"><div class="art" style="background:linear-gradient(200deg,#f0a27a,#e8663e 50%,transparent)" role="img" aria-label="Orange striped towel"></div><span class="label">TOWEL - CORALLUNE</span><span class="pill outline">Shop Now <svg width="32" height="8" style="color:#2b2265"><use href="#arrow"/></svg></span></div>
  <div class="abs cat" style="left:759px"><div class="art" style="background:linear-gradient(200deg,#d9b09a,#8eb1b0 55%,transparent)" role="img" aria-label="Patterned bucket hat"></div><span class="label">BUCKETS - CORALLUNE</span><span class="pill outline">Shop Now <svg width="32" height="8" style="color:#2b2265"><use href="#arrow"/></svg></span></div>

  <!-- most selling -->
  <h2 class="abs display sec-title" style="top:1780px">MOST SELLING PRODUCTS</h2>
  <div class="abs pill solid see-all" style="top:1782px">See All <svg width="32" height="8" style="color:#fff"><use href="#arrow"/></svg></div>

  <article class="abs card md" style="left:150px;top:1830px;width:212px;height:217px"><div class="img" style="background:linear-gradient(180deg,#eacfd3,#f0c98a 55%,#e7c3c6)" role="img" aria-label="Striped beach bag"></div><span class="heart"><svg width="10" height="10"><use href="#heart"/></svg></span><div class="info"><div class="row"><span>Bag - Lorem Ipsum</span><span>€ 16.90</span></div><div class="meta">6 Different Designs Available</div><div class="stars">★★★★★ <em>(12)</em></div><span class="cta">Add to cart</span></div></article>
  <article class="abs card md" style="left:379px;top:1830px;width:213px;height:217px"><div class="img" style="background:linear-gradient(180deg,#7faab6,#c7b59c 55%,#8aaab2)" role="img" aria-label="Patterned bucket hat"></div><span class="heart"><svg width="10" height="10"><use href="#heart"/></svg></span><div class="info"><div class="row"><span>Bucket - Lorem Ipsum</span><span>€ 16.90</span></div><div class="meta">6 Different Designs Available</div><div class="stars">★★★★★ <em>(12)</em></div><span class="cta">Add to cart</span></div></article>
  <article class="abs card md" style="left:608px;top:1830px;width:213px;height:217px"><div class="img" style="background:linear-gradient(180deg,#ececee,#3f3d4e 55%,#e0e0e4)" role="img" aria-label="Dark patterned cap"></div><span class="heart"><svg width="10" height="10"><use href="#heart"/></svg></span><div class="info"><div class="row"><span>Jokey - Cap</span><span>€ 16.90</span></div><div class="meta">6 Different Designs Available</div><div class="stars">★★★★★ <em>(12)</em></div><span class="cta">Add to cart</span></div></article>
  <article class="abs card md" style="left:836px;top:1830px;width:214px;height:217px"><div class="img" style="background:linear-gradient(160deg,#e6e4e0,#f5efe4 50%,#e9d6b8)" role="img" aria-label="Cream pouch with fruit print"></div><span class="heart"><svg width="10" height="10"><use href="#heart"/></svg></span><div class="info"><div class="row"><span>Pouch - Lorem Ipsum</span><span>€ 16.90</span></div><div class="meta">6 Different Designs Available</div><div class="stars">★★★★★ <em>(12)</em></div><span class="cta">Add to cart</span></div></article>
  <article class="abs card md" style="left:150px;top:2065px;width:212px;height:217px"><div class="img" style="background:linear-gradient(180deg,#eaa54a,#f1ead8 50%,#e9a24a)" role="img" aria-label="White tote bag on orange"></div><span class="heart"><svg width="10" height="10"><use href="#heart"/></svg></span><div class="info"><div class="row"><span>Bag - Lorem Ipsum</span><span>€ 16.90</span></div><div class="meta">6 Different Designs Available</div><div class="stars">★★★★★ <em>(12)</em></div><span class="cta">Add to cart</span></div></article>
  <article class="abs card md" style="left:379px;top:2065px;width:213px;height:217px"><div class="img" style="background:linear-gradient(170deg,#f4f4f6,#9fd6b8 40%,#c9b3e0 60%,#f4f4f6)" role="img" aria-label="Pastel striped beach towel"></div><span class="heart"><svg width="10" height="10"><use href="#heart"/></svg></span><div class="info"><div class="row"><span>Towel - Lorem Ipsum</span><span>€ 16.90</span></div><div class="meta">6 Different Designs Available</div><div class="stars">★★★★★ <em>(12)</em></div><span class="cta">Add to cart</span></div></article>
  <article class="abs card md" style="left:608px;top:2065px;width:213px;height:217px"><div class="img" style="background:radial-gradient(circle at 50% 50%,#2b2b2b,#e6e2da 35%,#7fc3b6 65%)" role="img" aria-label="Black and white scrunchie on teal"></div><span class="heart"><svg width="10" height="10"><use href="#heart"/></svg></span><div class="info"><div class="row"><span>Scrunches - Lorem Ipsum</span><span>€ 16.90</span></div><div class="meta">6 Different Designs Available</div><div class="stars">★★★★★ <em>(12)</em></div><span class="cta">Add to cart</span></div></article>
  <article class="abs card md" style="left:836px;top:2065px;width:214px;height:217px"><div class="img" style="background:linear-gradient(180deg,#7d9fb4,#d98a64 50%,#7d9fb4)" role="img" aria-label="Floral bucket hat"></div><span class="heart"><svg width="10" height="10"><use href="#heart"/></svg></span><div class="info"><div class="row"><span>Pouch - Lorem Ipsum</span><span>€ 16.90</span></div><div class="meta">6 Different Designs Available</div><div class="stars">★★★★★ <em>(12)</em></div><span class="cta">Add to cart</span></div></article>

  <!-- services -->
  <h2 class="abs display sec-title" style="top:2318px">SERVICES TO HELP YOU SHOP</h2>
  <article class="abs service" style="left:150px"><div class="photo" style="background:linear-gradient(160deg,#3a3a3a,#6b5a4a 50%,#2e2a28)" role="img" aria-label="Audience raising hands at an event"></div><h4>Frequently Asked Questions</h4><p>Updates on safe shopping on our store</p><span class="cta">Read More</span></article>
  <article class="abs service" style="left:455px"><div class="photo" style="background:linear-gradient(160deg,#b89a7a,#8a6a52 50%,#d0b48e)" role="img" aria-label="Courier handing a parcel to a customer"></div><h4>Home Delivery Options</h4><p>Updates on safe shopping on our store</p><span class="cta">Read More</span></article>
  <article class="abs service" style="left:760px"><div class="photo" style="background:linear-gradient(160deg,#e4e2dc,#6a7c9a 55%,#bdb8ae)" role="img" aria-label="Person on a sofa paying online with a card"></div><h4>Online Payment Process</h4><p>Updates on safe shopping on our store</p><span class="cta">Read More</span></article>

  <!-- footer -->
  <footer class="abs footer"></footer>
  <nav class="abs f-links"><span>Terms of Services</span><span>Privacy Policy</span><span>Site Map</span></nav>
  <div class="abs follow">Follow Us <i></i><i></i><i></i><i></i></div>
  <div class="abs rule" style="top:2750px"></div>
  <div class="abs f-col" style="left:150px"><h5>ABOUT</h5><ul><li>About Us</li><li>Services</li><li>Terms of Service</li></ul></div>
  <div class="abs f-col" style="left:383px"><h5>CATEGORIES</h5><ul><li>Bags</li><li>Jokey caps</li><li>Scrunches</li><li>Tote bags</li><li>Hat</li><li>Towel</li></ul></div>
  <div class="abs f-col" style="left:611px"><h5>SUPPORT</h5><ul><li>Help &amp; Support</li><li>FAQ's</li><li>Contact Us</li><li>Services</li></ul></div>
  <div class="abs f-col" style="left:832px"><h5>SUBSCRIBE</h5></div>
  <div class="abs subscribe"><span>Submit</span></div>
  <div class="abs f-col" style="left:832px;top:2858px"><h5>APPS</h5></div>
  <div class="abs app" style="top:2893px"><i></i>IOS App</div>
  <div class="abs app" style="top:2920px"><i></i>Android App</div>
  <div class="abs rule" style="top:3000px"></div>
  <div class="abs copy">Copyright © 2022 Corallune - SummerWear</div>

</div>
</body>
</html>
```